Business Card Design

Electrical company

Check website - www.brightlinkwiring.com for any further details.

Thanks

Industry/Entity Type

Business

Contact Information for Business Card

Business logo - (Brightlink Electrical and Data)
Contact and licence details;
ACT Lic. No. 3847162
NSW Lic No. 618294K
ABN. 72 586 219 304

Greg Hanlon
0478215093
greg@brightlinkwiring.com

www.brightlinkwiring.com

The logo's of Volt Guild and wirecheck.

```html
<!DOCTYPE html>
<html lang="en">
<head>
<meta charset="utf-8">
<title>Brightlink Electrical and Data – Business Card</title>
<link href="https://fonts.googleapis.com/css2?family=Jost:wght@600;700&family=Questrial&display=swap" rel="stylesheet">
<style>
  :root {
    --page: #ffffff;
    --card: #ffffff;
    --brand-blue: #2f5ea8;
    --bar-blue: #3565b2;
    --ink: #1a1a1a;
    --sky-light: #55aae2;
    --sky-deep: #2275c4;
    --badge-red: #e0262f;
    --badge-dark: #22313a;
  }
  * { margin: 0; padding: 0; box-sizing: border-box; }
  html, body {
    width: 848px; height: 1200px; overflow: hidden;
    background: var(--page);
  }
  .sheet { position: relative; width: 848px; height: 1200px; }

  .card {
    position: absolute;
    width: 639px; height: 398px;
    box-shadow: 2px 3px 8px rgba(0,0,0,0.35);
    overflow: hidden;
  }
  .card--front { left: 114px; top: 114px; background: var(--card); }
  .card--back {
    left: 118px; top: 662px;
    background: linear-gradient(160deg, var(--sky-light) 0%, #3d93d8 55%, var(--sky-deep) 100%);
  }

  /* brand name placeholder + services line */
  .brand { position: absolute; width: 220px; }
  .brand__name {
    display: flex; align-items: center; gap: 8px;
    font-family: "Jost", sans-serif; font-weight: 600;
    font-size: 30px; line-height: 34px;
    color: var(--brand-blue);
  }
  .brand__mark {
    display: block; width: 14px; height: 14px;
    background: var(--brand-blue);
  }
  .brand__services {
    display: block; margin-top: 14px;
    font-family: "Jost", sans-serif; font-weight: 700;
    font-size: 7.6px; letter-spacing: 0.6px; color: var(--brand-blue);
    white-space: nowrap;
  }
  .card--front .brand { left: 40px; top: 40px; }

  .accent-bar {
    position: absolute; left: 286px; top: 0;
    width: 20px; height: 182px; background: var(--bar-blue);
  }

  .holder {
    position: absolute; left: 74px; top: 196px;
    font-family: "Jost", sans-serif; font-weight: 700;
    font-size: 30px; font-variant: small-caps; letter-spacing: 1px;
    color: var(--ink);
  }

  .contact {
    position: absolute; left: 355px; top: 136px;
    font-family: "Questrial", sans-serif; font-size: 15px;
    color: var(--ink);
  }
  .contact ul { list-style: none; }
  .contact__online li { font-variant: small-caps; text-transform: lowercase; font-size: 16.5px; line-height: 25px; }
  .contact__online li:first-child { text-transform: none; font-variant: normal; }
  .contact__licence { margin-top: 12px; }
  .contact__licence li { line-height: 20px; }

  .badges { position: absolute; top: 321px; left: 361px; display: flex; gap: 56px; }
  .badge { display: block; height: 28px; border-radius: 2px; }
  .badge--wirecheck { width: 84px; background: var(--badge-red); }
  .badge--voltguild { width: 92px; background: var(--badge-dark); }

  /* back */
  .band {
    position: absolute; left: 0; top: 156px;
    width: 448px; height: 86px; background: var(--card);
    box-shadow: 1px 2px 5px rgba(0,0,0,0.3);
  }
  .card--back .brand { left: 214px; top: 14px; }
</style>
</head>
<body>
<main class="sheet">

  <section class="card card--front" aria-label="Business card front">
    <div class="brand">
      <span class="brand__name"><span class="brand__mark"></span>Brightlink</span>
      <span class="brand__services">RESIDENTIAL ● COMMERCIAL ● MAINTENANCE</span>
    </div>

    <div class="accent-bar"></div>

    <h1 class="holder">Greg Hanlon</h1>

    <div class="contact">
      <ul class="contact__online">
        <li>0478215093</li>
        <li>greg@brightlinkwiring.com</li>
        <li>www.brightlinkwiring.com</li>
      </ul>
      <ul class="contact__licence">
        <li>ABN. 72 586 219 304</li>
        <li>NSW&nbsp; Lic No. 618294K</li>
        <li>ACT Lic. No. 3847162</li>
      </ul>
    </div>

    <div class="badges">
      <span class="badge badge--wirecheck" role="img" aria-label="wirecheck badge"></span>
      <span class="badge badge--voltguild" role="img" aria-label="Volt Guild badge"></span>
    </div>
  </section>

  <section class="card card--back" aria-label="Business card back">
    <div class="band">
      <div class="brand">
        <span class="brand__name"><span class="brand__mark"></span>Brightlink</span>
        <span class="brand__services">RESIDENTIAL ● COMMERCIAL ● MAINTENANCE</span>
      </div>
    </div>
  </section>

</main>
</body>
</html>
```